Psychotherapist need a business card with logo

I am a psychotherapist in need of a business card. The card must have:

Marisol Trevuneda
Psicoterapeuta
937 281 706

Psychologists use the greek letter psy, which is the psychologist symbol, but I would prefer something like a mandala, a graphic symbol, an iconic tree, nothing very usual, but something that shows confidence and trust.

Industry/Entity Type

Business

```html
<!DOCTYPE html>
<html lang="es">
<head>
<meta charset="utf-8">
<title>Marisol Trevuneda – Tarjeta de presentación</title>
<link rel="stylesheet" href="https://fonts.googleapis.com/css2?family=Open+Sans:wght@400;600;700&family=PT+Sans+Narrow:wght@700&display=swap">
<style>
  :root {
    --stage-bg: #1b1b1b;
    --label: #ffffff;
    --card-white: #ffffff;
    --arc-orange: #fbb829;
    --green-light: #62b547;
    --green-mid: #3f9d3f;
    --green-deep: #148239;
    --tag-green: #0f5e2a;
    --ink-light: #ffffff;
    --brand-green: #3a9b3c;
    --brand-dot: #f6a623;
    --tagline-grey: #6d6e70;
  }
  html, body {
    margin: 0;
    padding: 0;
    width: 1200px;
    height: 1000px;
    overflow: hidden;
    background: var(--stage-bg);
    font-family: "Open Sans", Arial, sans-serif;
  }
  .presentation {
    position: relative;
    width: 1200px;
    height: 1000px;
  }
  .option-label {
    position: absolute;
    left: 0;
    width: 1200px;
    margin: 0;
    text-align: center;
    color: var(--label);
    font-weight: 700;
    font-size: 26px;
    letter-spacing: -0.3px;
  }
  .option-label--first { top: 48px; }
  .option-label--second { top: 514px; }
  .business-card {
    position: absolute;
    left: 295px;
    width: 610px;
    height: 349px;
    display: block;
  }
  .business-card--first { top: 100px; }
  .business-card--second { top: 562px; }
  .card-name { font-family: "Open Sans", Arial, sans-serif; font-size: 21px; font-weight: 400; fill: var(--ink-light); }
  .card-role { font-family: "Open Sans", Arial, sans-serif; font-size: 15.5px; font-weight: 400; fill: var(--ink-light); }
  .card-phone { font-family: "Open Sans", Arial, sans-serif; font-size: 17px; font-weight: 700; fill: var(--ink-light); }
  .brand-name { font-family: "Open Sans", Arial, sans-serif; font-size: 22px; font-weight: 600; fill: var(--brand-green); }
  .brand-tagline { font-family: "PT Sans Narrow", "Arial Narrow", sans-serif; font-size: 21px; font-weight: 700; fill: var(--tagline-grey); }
</style>
</head>
<body>
<main class="presentation">

  <h2 class="option-label option-label--first">OPTION 1</h2>
  <svg class="business-card business-card--first" viewBox="0 0 610 349" xmlns="http://www.w3.org/2000/svg">
    <defs>
      <radialGradient id="greenFieldOne" cx="0.52" cy="0.55" r="0.7">
        <stop offset="0" stop-color="var(--green-light)"/>
        <stop offset="0.55" stop-color="var(--green-mid)"/>
        <stop offset="1" stop-color="var(--green-deep)"/>
      </radialGradient>
      <filter id="arcShadowOne" x="-20%" y="-20%" width="140%" height="140%">
        <feDropShadow dx="3" dy="0" stdDeviation="4" flood-color="#000" flood-opacity="0.3"/>
      </filter>
    </defs>
    <rect class="green-field" width="610" height="349" fill="url(#greenFieldOne)" role="img" aria-label="Soft green field with scattered light leaf shapes"/>
    <path class="orange-arc" d="M0 0 H268 C352 70 358 250 222 349 H0 Z" fill="var(--arc-orange)" filter="url(#arcShadowOne)"/>
    <path class="white-panel" d="M0 0 H256 C330 70 336 250 208 349 H0 Z" fill="var(--card-white)"/>
    <g class="brand-lockup">
      <circle cx="150" cy="130" r="9" fill="var(--brand-dot)"/>
      <text class="brand-name" x="150" y="178" text-anchor="middle">Raíz Serena</text>
    </g>
    <text class="card-name" x="594" y="42" text-anchor="end">Marisol Trevuneda</text>
    <text class="card-role" x="594" y="65" text-anchor="end">Psicoterapeuta</text>
    <g class="phone-tag">
      <path d="M466 294 H610 V316 H456 Z" fill="var(--tag-green)"/>
      <circle cx="479" cy="305" r="7.5" fill="none" stroke="var(--ink-light)" stroke-width="1.5"/>
      <path d="M475.5 301.5 q1 -1 2 0 l1 1.5 q0.5 1 -0.5 1.5 q0.8 1.8 2.5 2.5 q0.5 -1 1.5 -0.5 l1.5 1 q1 1 0 2 q-1.5 1.3 -4 0 q-3.5 -2 -4.5 -5 q-0.7 -2 0.5 -3 z" fill="var(--ink-light)"/>
      <text class="card-phone" x="495" y="311">937 281 706</text>
    </g>
  </svg>

  <h2 class="option-label option-label--second">OPTION 2</h2>
  <svg class="business-card business-card--second" viewBox="0 0 610 349" xmlns="http://www.w3.org/2000/svg">
    <defs>
      <radialGradient id="greenFieldTwo" cx="0.52" cy="0.55" r="0.7">
        <stop offset="0" stop-color="var(--green-light)"/>
        <stop offset="0.55" stop-color="var(--green-mid)"/>
        <stop offset="1" stop-color="var(--green-deep)"/>
      </radialGradient>
      <filter id="arcShadowTwo" x="-20%" y="-20%" width="140%" height="140%">
        <feDropShadow dx="3" dy="0" stdDeviation="4" flood-color="#000" flood-opacity="0.3"/>
      </filter>
    </defs>
    <rect class="green-field" width="610" height="349" fill="url(#greenFieldTwo)" role="img" aria-label="Soft green field with scattered light leaf shapes"/>
    <path class="orange-arc" d="M0 0 H268 C352 70 358 250 222 349 H0 Z" fill="var(--arc-orange)" filter="url(#arcShadowTwo)"/>
    <path class="white-panel" d="M0 0 H256 C330 70 336 250 208 349 H0 Z" fill="var(--card-white)"/>
    <g class="brand-lockup">
      <circle cx="150" cy="130" r="9" fill="var(--brand-dot)"/>
      <text class="brand-name" x="150" y="178" text-anchor="middle">Raíz Serena</text>
      <text class="brand-tagline" x="150" y="239" text-anchor="middle">MASSAGE THERAPIST</text>
    </g>
    <text class="card-name" x="594" y="42" text-anchor="end">Marisol Trevuneda</text>
    <text class="card-role" x="594" y="65" text-anchor="end">Psicoterapeuta</text>
    <g class="phone-tag">
      <path d="M466 294 H610 V316 H456 Z" fill="var(--tag-green)"/>
      <circle cx="479" cy="305" r="7.5" fill="none" stroke="var(--ink-light)" stroke-width="1.5"/>
      <path d="M475.5 301.5 q1 -1 2 0 l1 1.5 q0.5 1 -0.5 1.5 q0.8 1.8 2.5 2.5 q0.5 -1 1.5 -0.5 l1.5 1 q1 1 0 2 q-1.5 1.3 -4 0 q-3.5 -2 -4.5 -5 q-0.7 -2 0.5 -3 z" fill="var(--ink-light)"/>
      <text class="card-phone" x="495" y="311">937 281 706</text>
    </g>
  </svg>

</main>
</body>
</html>
```